Creative Wedding invitation with a roadmap needs a designer

Dear,

we two are from germany and are going to marry in our hometown croatia.
our guests will come from germany and some of them are locals.

We want to make a creative wedding invitation and for orientation to have the guests a small roadmap with our cellphone number on it and the 4 spots where everything will happen and a small timetable (programm)

The cardboard should be white with a silver or chrome effect color cut
The plasticcard should be silver or silver glitter on the front names + date on the backside a roadmap where the guests can see where the spots will be.

We attached you a sketch of our idea.

Basically its about a White DIN B6 Card with an extra envelope, centered on the Cardboard with a gluespot and a plastic card.

Thank you so much!

Mariella & Dominik
Updates

Target Market(s)

Wedding invitation

Industry/Entity Type

Wedding

Font styles to use
Serif
Decorative
Script

Requirements
Must have
• The cardboard should be white with a silver or chrome effect color cut
• The plasticcard should be silver or silver glitter on the front names + date on the backside a roadmap
Nice to have
• Translucent elements
• Colors: White, Silver, Glitter, Translucent
• Hologram with our the date or M&D

```html
<!DOCTYPE html>
<html lang="en">
<head>
<meta charset="utf-8">
<title>Mariella &amp; Dominik – Wedding Invitation</title>
<link rel="stylesheet" href="https://fonts.googleapis.com/css2?family=Great+Vibes&family=EB+Garamond:ital@0;1&family=Arimo&display=swap">
<style>
  :root {
    --ink: #111111;
    --card-black: #262626;
    --panel-grey: #bdbdbd;
    --paper-white: #ffffff;
    --pearl: #f2f1ee;
    --silver-light: #d8d8d8;
    --silver-mid: #9a9a9a;
    --silver-dark: #5a5a5a;
    --glitter-gold: #b8ab8c;
    --stage-dark: #0c0c0c;
    --stage-light: #bdbdbd;
  }
  * { margin: 0; padding: 0; box-sizing: border-box; }
  html, body { width: 1200px; height: 852px; overflow: hidden; background: var(--paper-white); }
  .canvas { position: relative; width: 1200px; height: 852px; }

  .stage {
    position: absolute; left: 0; top: 0; width: 1200px; height: 800px;
    background: linear-gradient(90deg, var(--stage-dark) 0%, var(--stage-dark) 55%, var(--stage-light) 100%);
  }

  /* Pocket folder */
  .envelope {
    position: absolute; left: 0; top: 0; width: 330px; height: 260px;
    background: linear-gradient(160deg, var(--pearl), var(--silver-light));
  }
  .pocket {
    position: absolute; left: 0; top: 30px; width: 450px; height: 770px;
    background: linear-gradient(135deg, var(--silver-light) 0%, var(--silver-mid) 45%, var(--silver-dark) 100%);
  }
  .pocket-flap {
    position: absolute; left: 410px; top: 100px; width: 80px; height: 700px;
    background: linear-gradient(180deg, var(--silver-mid), var(--silver-dark));
  }
  .monogram-frame {
    position: absolute; left: 188px; top: 240px; width: 376px; height: 384px;
    background: var(--ink);
  }
  .monogram-plate {
    position: absolute; left: 24px; top: 16px; width: 332px; height: 344px;
    background: var(--pearl);
    display: flex; align-items: center; justify-content: center;
  }
  .monogram-art {
    width: 220px; height: 240px;
    background: radial-gradient(ellipse at center, #d9d8d5 0%, var(--pearl) 75%);
  }

  /* Invitation card */
  .invitation {
    position: absolute; left: 600px; top: 46px; width: 530px; height: 714px;
    background: var(--card-black);
  }
  .invitation-panel {
    position: absolute; left: 30px; top: 30px; width: 474px; height: 648px;
    border: 8px solid var(--paper-white); border-radius: 26px;
    background: var(--panel-grey); overflow: hidden;
  }
  .couple-name {
    position: absolute; left: 0; width: 100%;
    font-family: "Great Vibes", cursive; color: var(--paper-white);
    font-size: 128px; line-height: 1; text-align: center;
  }
  .couple-name--first { top: 40px; }
  .couple-name--second { top: 190px; }
  .ampersand {
    position: absolute; top: 145px; left: 0; width: 100%; text-align: center;
    font-family: "Great Vibes", cursive; color: var(--paper-white); font-size: 40px;
  }

  .invitation-text {
    position: absolute; left: 0; top: 488px; width: 100%;
    font-family: "EB Garamond", serif; color: var(--paper-white);
    font-size: 18px; line-height: 24px; white-space: nowrap;
  }
  .text-line { display: flex; justify-content: center; }
  .text-line .left { flex: 1; text-align: right; }
  .text-line .right { flex: 1; text-align: left; }
  .text-line .gap--wide { width: 104px; }
  .text-line .gap--narrow { width: 56px; }
  .text-line--italic { font-style: italic; font-size: 17px; line-height: 35px; }

  .glitter-band {
    position: absolute; left: 600px; top: 480px; width: 530px; height: 84px;
    background: linear-gradient(90deg, var(--silver-mid), var(--glitter-gold) 30%, var(--silver-light) 55%, var(--glitter-gold) 80%, var(--silver-mid));
  }
  .date-badge { position: absolute; left: 757px; top: 410px; width: 220px; height: 220px; }
  .date-text {
    position: absolute; left: 767px; top: 476px; width: 200px; text-align: center;
    font-family: "EB Garamond", serif; font-style: italic; font-size: 32px; line-height: 44px;
    color: var(--ink);
  }

  .caption {
    position: absolute; left: 16px; top: 804px;
    font-family: "Arimo", sans-serif; font-size: 32px; color: var(--ink);
  }
</style>
</head>
<body>
<div class="canvas">
  <div class="stage"></div>

  <div class="envelope"></div>
  <div class="pocket"></div>
  <div class="pocket-flap"></div>
  <div class="monogram-frame">
    <div class="monogram-plate">
      <div class="monogram-art" role="img" aria-label="Flourished script monogram M&amp;D in black"></div>
    </div>
  </div>

  <div class="invitation">
    <div class="invitation-panel">
      <div class="couple-name couple-name--first">Mariella</div>
      <div class="ampersand">&amp;</div>
      <div class="couple-name couple-name--second">Dominik</div>
      <div class="invitation-text">
        <div class="text-line"><span class="left">Ut enim ad minim</span><span class="gap--wide"></span><span class="right">quis nostrud ullamco</span></div>
        <div class="text-line"><span class="left">exercitation ullamco</span><span class="gap--narrow"></span><span class="right">nisi ut aliquip ex ea</span></div>
        <div class="text-line">commodo consequat. Duis aute irure dolor in</div>
        <div class="text-line text-line--italic">reprehenderit in voluptate velit esse cillum dolore</div>
        <div class="text-line text-line--italic">eu fugiat nulla pariatur.</div>
      </div>
    </div>
  </div>

  <div class="glitter-band"></div>
  <svg class="date-badge" viewBox="0 0 220 220" aria-hidden="true">
    <rect x="36" y="36" width="148" height="148" transform="rotate(45 110 110)" fill="#111111"/>
    <rect x="48" y="48" width="124" height="124" transform="rotate(45 110 110)" fill="#ffffff"/>
  </svg>
  <div class="date-text">30.07.<br>2017</div>

  <p class="caption">Black craft paper. Transparency paper with white print.</p>
</div>
</body>
</html>
```